Business Card

We need some ideas for corporate business cards. I'm interested in a double sided card, with one side featuring our corporate logo, the other side with employee information.

Corporate colors, logo etc. available at www.brivalo.com

Industry/Entity Type

Business

Requirements
Must have
• The "Brivalo" logo with stylized "O"

Nice to have
• Preferred font is calibri

```html
<!DOCTYPE html>
<html lang="en">
<head>
<meta charset="utf-8">
<title>Brivalo Business Card – Sample Design</title>
<link rel="stylesheet" href="https://fonts.googleapis.com/css2?family=Nunito+Sans:wght@300;400;600;700&display=swap">
<style>
  :root {
    --brand-blue: #4a5f91;
    --brand-blue-light: #6a7daf;
    --paper: #ffffff;
    --ink-light: #ffffff;
  }
  * { margin: 0; padding: 0; box-sizing: border-box; }
  html, body {
    width: 1200px; height: 1000px; overflow: hidden;
    background: var(--paper);
    font-family: "Nunito Sans", "Avenir Next", Arial, sans-serif;
  }
  .canvas { position: relative; width: 1200px; height: 1000px; }
  .page-title {
    position: absolute; top: 78px; left: 0; width: 100%;
    text-align: center; font-weight: 400; font-size: 44px;
    color: var(--brand-blue); letter-spacing: 0.5px;
  }
  .card {
    position: absolute; background: var(--brand-blue);
    color: var(--ink-light); overflow: hidden;
  }
  .card--landscape { left: 27px; top: 223px; width: 691px; height: 380px; }
  .card--portrait { left: 771px; top: 223px; width: 380px; height: 690px; }
  .brand-graphic-area { position: absolute; left: 0; top: 0; }
  .brand-name {
    position: absolute; font-weight: 700; font-size: 40px;
    letter-spacing: 7px; line-height: 1; white-space: nowrap;
    transform: rotate(37deg); transform-origin: left top;
  }
  .brand-url {
    position: absolute; font-weight: 400; font-size: 16px;
    line-height: 1; white-space: nowrap; letter-spacing: 0.5px;
    transform: rotate(-53deg); transform-origin: left bottom;
  }
  .contact { position: absolute; text-align: right; font-weight: 300; }
  .contact__name { font-size: 34px; font-weight: 400; line-height: 1.1; padding-right: 7px; }
  .contact__role { font-size: 17px; line-height: 1.2; padding-right: 7px; }
  .contact__address { font-size: 17px; line-height: 21.5px; margin-top: 66px; }
  .contact__lines { font-size: 15px; line-height: 20px; margin-top: 20px; }
  .card--landscape .contact { right: 43px; top: 66px; width: 360px; }
  .card--portrait .contact { right: 26px; top: 373px; width: 360px; }
  .card--portrait .contact__address { margin-top: 52px; }
</style>
</head>
<body>
<main class="canvas">
  <h1 class="page-title">Sample Design</h1>

  <section class="card card--landscape" aria-label="Business card, landscape">
    <svg class="brand-graphic-area" width="400" height="380" viewBox="0 0 400 380" role="img" aria-label="Area for the large brand graphic">
      <defs>
        <linearGradient id="graphicToneA" x1="0" y1="0" x2="1" y2="0">
          <stop offset="0" stop-color="var(--brand-blue-light)"/>
          <stop offset="1" stop-color="var(--brand-blue)"/>
        </linearGradient>
      </defs>
      <rect x="0" y="0" width="400" height="380" fill="url(#graphicToneA)"/>
    </svg>
    <div class="brand-name" style="left:132px; top:20px;">BRIVALO</div>
    <div class="brand-url" style="left:175px; top:287px;">www.brivalo.com</div>

    <div class="contact">
      <div class="contact__name">Your Name</div>
      <div class="contact__role">Manajer</div>
      <div class="contact__address">
        Brivalo<br>9 Larkin Row, Hollybrook Business<br>Park, Dublin 14<br>Dublin, DB<br>Ireland
      </div>
      <div class="contact__lines">
        Tel: +353 1 555 0142<br>Fax: +353 1 555 0199
      </div>
    </div>
  </section>

  <section class="card card--portrait" aria-label="Business card, portrait">
    <svg class="brand-graphic-area" width="380" height="370" viewBox="0 0 380 370" role="img" aria-label="Area for the large brand graphic">
      <defs>
        <linearGradient id="graphicToneB" x1="0" y1="0" x2="0" y2="1">
          <stop offset="0" stop-color="var(--brand-blue-light)"/>
          <stop offset="1" stop-color="var(--brand-blue)"/>
        </linearGradient>
      </defs>
      <rect x="0" y="0" width="380" height="370" fill="url(#graphicToneB)"/>
    </svg>
    <div class="brand-name" style="left:166px; top:20px;">BRIVALO</div>
    <div class="brand-url" style="left:212px; top:276px;">www.brivalo.com</div>

    <div class="contact">
      <div class="contact__name">Your Name</div>
      <div class="contact__role">Manajer</div>
      <div class="contact__address">
        Brivalo<br>9 Larkin Row, Hollybrook Business<br>Park, Dublin 14<br>Dublin, DB<br>Ireland
      </div>
      <div class="contact__lines">
        Tel: +353 1 555 0142<br>Fax: +353 1 555 0199
      </div>
    </div>
  </section>
</main>
</body>
</html>
```